New Technology Company is Launching New Products with a New Website

We want to create a 4-page website in WordPress compatible files to launch our site on HostWeave. The attached files provide our ideas for Products, Services and About Us pages. We believe the content in those files is about right but the actual design is up to the artist that wants to accept this challenge. Additionally we need a fantastic Home page but we have no idea what that looks like. It obviously needs to lead to the other 3 pages but more importantly it needs to capture the interest of our current and future customers.

Details:
1. Please start off using the text descriptions in the example files. If shorter, longer, different descriptions are needed, just let us know.

2. Please feel free to suggest any photos you can find from free or reasonable stock photo services. Pixelbarn and others like them are reasonable. If you find a perfect image, please send us a link and we will buy a license if its affordable. I have paid ~US$10 per image in the past.

3. I have also uploaded our stationery and logo files. We would like the website design to be consistent with the logo and stationery designs. The stationery designs are all in one file.

We have two logos, and would like to see both of them used on the website. One logo shows the letters KRVT in an outlined shield that is read and blue. That logo is used in the stationery and in our draft website design as a header. The other logo shows flames bouncing off a round shield. Perhaps this logo could be used at the bottom of each page on the website, or some other place where it would be fun and creative without diminishing the seriousness of our underlying science and engineering.

4. We are looking for an artist to have some fun with this and propose something creative. We have lots of boring ideas ourselves so we need YOU to do something else! Thank you so much for considering this challenge!

Target Market(s)

People interested in new, high performance fabrics, including consumers, store owners, garment designers and companies like Velorina or The Copper Loom

Coding

Coded - Design and coding required

Font styles to use
Sans Serif

Colors
f04a51
3277b5

Requirements
Must have
• something unforgetable

```html
<!DOCTYPE html>
<html lang="en">
<head>
<meta charset="utf-8">
<title>KRVT — Products</title>
<link rel="stylesheet" href="https://fonts.googleapis.com/css2?family=Open+Sans:wght@400;600;700&family=Montserrat:wght@600;700&display=swap">
<style>
:root{
  --red:#f04a51;
  --blue:#3277b5;
  --ink:#4a4f55;
  --muted:#7b8087;
  --rule:#e3e6ea;
  --band:#eef1f4;
  --footer:#2a2d31;
  --white:#ffffff;
}
*{box-sizing:border-box;margin:0;padding:0}
html,body{width:1200px;height:2368px;overflow:hidden}
body{position:relative;background:var(--white);font-family:"Open Sans",Arial,sans-serif;color:var(--ink)}
.abs{position:absolute}

.site-header{left:0;top:0;width:1200px;height:96px}
.brand{left:120px;top:22px;display:flex;align-items:center;gap:12px}
.brand-mark{width:40px;height:40px;background:var(--red);border-radius:50%}
.brand-name{font-family:"Montserrat",sans-serif;font-weight:700;font-size:34px;color:var(--blue);letter-spacing:1px}
.contact-panel{right:0;top:0;width:420px;height:62px}
.contact-panel svg{position:absolute;left:0;top:0}
.contact-text{position:absolute;right:120px;top:6px;text-align:right;color:var(--white);font-size:10px;line-height:13px}
.contact-text .company{font-family:"Montserrat",sans-serif;font-size:12px;font-weight:700;letter-spacing:.5px}
.main-nav{left:330px;top:66px;display:flex;gap:24px;font-size:11px;font-weight:600;text-transform:uppercase;letter-spacing:.6px;color:var(--muted)}
.main-nav .active{color:var(--red)}
.header-rule{left:0;top:96px;width:1200px;height:3px;background:var(--red)}

.page-title{left:0;top:208px;width:1200px;text-align:center;font-family:"Montserrat",sans-serif;font-weight:700;font-size:30px;color:var(--red);letter-spacing:1px}
.section-title{left:0;width:1200px;text-align:center;font-family:"Montserrat",sans-serif;font-weight:700;font-size:22px;color:var(--blue);letter-spacing:.8px}
.section-title.hot{color:var(--red)}
.section-copy{left:300px;width:600px;text-align:center;font-size:11.5px;line-height:19px;color:var(--ink)}
.section-copy.wide{left:250px;width:700px}
.cta{left:0;width:1200px;text-align:center;font-size:11.5px;color:var(--ink)}
.media{width:300px}
.photo{height:100%}
.divider{left:300px;width:600px;height:1px;background:var(--rule)}
.band{left:0;top:1780px;width:1200px;height:400px;background:var(--band)}

.site-footer{left:0;top:2256px;width:1200px;height:112px;background:var(--footer)}
.footer-brand{left:120px;top:34px;display:flex;align-items:center;gap:10px}
.footer-brand .mark{width:36px;height:36px;border-radius:50%;background:var(--red)}
.footer-brand .name{font-family:"Montserrat",sans-serif;font-weight:700;font-size:22px;color:var(--white)}
.footer-nav{left:250px;top:40px;display:flex;gap:14px;font-size:10px;color:#c9ccd0}
.copyright{left:250px;top:60px;font-size:9.5px;color:#8d9197}
.social{right:120px;top:40px;display:flex;gap:10px}
.social span{width:26px;height:26px;border-radius:50%;background:var(--blue)}
</style>
</head>
<body>

<header class="site-header abs">
  <div class="brand abs"><span class="brand-mark"></span><span class="brand-name">KRVT</span></div>
  <div class="contact-panel abs">
    <svg width="420" height="62" viewBox="0 0 420 62" aria-hidden="true">
      <polygon points="34,0 420,0 420,62 0,62" fill="var(--blue)"/>
      <polygon points="34,0 46,0 12,62 0,62" fill="var(--red)"/>
    </svg>
    <div class="contact-text">
      <div class="company">K. R. VANTOR AND ASSOCIATES PLLC</div>
      <div>(555) 014-2290</div>
      <div>www.krvtlabs.com</div>
      <div>418 Halvern Way, Suite 2, Pinecrest, AZ 86000</div>
    </div>
  </div>
  <nav class="main-nav abs">
    <span>Home</span><span>About Us</span><span class="active">Products</span><span>Solutions</span><span>Contact Us</span>
  </nav>
</header>
<div class="header-rule abs"></div>

<h1 class="page-title abs">PRODUCTS</h1>

<h2 class="section-title abs" style="top:298px">HIGH – TEMPERATURE INSULATION</h2>
<p class="section-copy abs" style="top:340px">KRVT has been working on aerospace applications of high temperature insulations since the early hypersonic aircraft programs were first proposed decades ago. Back then we used gold and platinum to block heat. Today we make insulations that are much more affordable, more efficient and more reliable in Thermal Protection Systems.</p>
<p class="cta abs" style="top:432px">If this is what you need, contact us and ask about our OpenFibre Fibrous Insulation (OFI).</p>
<div class="media abs" style="left:300px;top:482px;height:200px">
  <div class="photo" role="img" aria-label="Heat shield glowing red under test flame in a dark test chamber" style="background:radial-gradient(ellipse at 50% 40%,#d8452c 0%,#7a1c12 45%,#140606 90%)"></div>
</div>
<div class="media abs" style="left:600px;top:482px;height:200px;background:#fff;border:1px solid var(--rule)">
  <svg width="298" height="198" viewBox="0 0 298 198" aria-label="Line chart of thermal conductivity against temperature">
    <line x1="40" y1="20" x2="40" y2="170" stroke="#555"/>
    <line x1="40" y1="170" x2="280" y2="170" stroke="#555"/>
    <g stroke="#ddd"><line x1="40" y1="132" x2="280" y2="132"/><line x1="40" y1="95" x2="280" y2="95"/><line x1="40" y1="58" x2="280" y2="58"/></g>
    <path d="M45 160 C120 150 190 120 270 40" stroke="#222" fill="none" stroke-width="1.5"/>
    <path d="M45 163 C130 156 200 138 270 90" stroke="#666" fill="none" stroke-width="1.5"/>
    <path d="M45 165 C140 160 210 152 270 130" stroke="#999" fill="none" stroke-width="1.5"/>
    <rect x="150" y="26" width="110" height="16" fill="#fff" stroke="#888"/>
    <text x="156" y="37" font-size="8" fill="#444" font-family="Open Sans,sans-serif">Thermal conductivity</text>
    <text x="120" y="190" font-size="8" fill="#444" font-family="Open Sans,sans-serif">Temperature (K)</text>
  </svg>
</div>
<div class="divider abs" style="top:728px"></div>

<h2 class="section-title abs" style="top:760px">AEROGEL INSULATIONS</h2>
<p class="section-copy abs" style="top:802px">KRVT has developed aerogel insulations that are thin, flexible and more than twice as warm as goose down. Although we developed these insulations for space suits and cryogenic tanks, we are very excited about their more earthly applications from cold weather clothing to industrial pipelines.</p>
<p class="cta abs" style="top:884px">If this is what you need, contact us and ask about our Fiber Reinforced Insulation with Aerogel (FRIA).</p>
<div class="media abs" style="left:300px;top:934px;height:240px;background:#fff;border:1px solid var(--rule)">
  <svg width="298" height="238" viewBox="0 0 298 238" aria-label="Bar chart comparing warmth of insulation materials">
    <line x1="40" y1="20" x2="40" y2="200" stroke="#888"/>
    <line x1="40" y1="200" x2="280" y2="200" stroke="#888"/>
    <rect x="60" y="150" width="28" height="50" fill="#4f81bd"/>
    <rect x="105" y="120" width="28" height="80" fill="#c0504d"/>
    <rect x="150" y="60" width="28" height="140" fill="#9bbb59"/>
    <rect x="195" y="95" width="28" height="105" fill="#8064a2"/>
    <rect x="240" y="135" width="28" height="65" fill="#4bacc6"/>
    <text x="110" y="222" font-size="8" fill="#444" font-family="Open Sans,sans-serif">Warmth per thickness</text>
  </svg>
</div>
<div class="media abs" style="left:600px;top:934px;height:240px">
  <div class="photo" role="img" aria-label="Mountaineer in a blue jacket climbing a snowy ridge under a bright sky" style="background:linear-gradient(180deg,#6fa7d8 0%,#a9cbe8 45%,#e9f1f8 70%,#c9d6e2 100%)"></div>
</div>
<div class="divider abs" style="top:1220px"></div>

<h2 class="section-title hot abs" style="top:1280px">FIRE RESISTANT FABRICS</h2>
<p class="section-copy abs" style="top:1322px">KRVT developed fire resistant fabrics and insulation blankets that provide serious levels of protection for fire fighters working a burn-over. The current shelter has saved many lives and prevented many injuries, but the tragic loss of a wildland crew in recent years motivated us to develop better fire shelters for today's wildfires that burn hotter and longer than those of decades ago.</p>
<p class="cta abs" style="top:1442px">If this is what you need, contact us and ask for the KRVT-100 FT, KRVT-X7 and KRVT-M2 fabrics.</p>
<div class="media abs" style="left:300px;top:1494px;height:220px">
  <div class="photo" role="img" aria-label="Wildfire flames burning through trees at night" style="background:radial-gradient(ellipse at 50% 65%,#f7a238 0%,#c6421a 35%,#3a0c06 80%)"></div>
</div>
<div class="media abs" style="left:600px;top:1494px;height:220px;background:#fff;border:1px solid var(--rule)">
  <svg width="298" height="218" viewBox="0 0 298 218" aria-label="Calorimeter test chart of heat flux over time">
    <text x="70" y="20" font-size="10" fill="var(--red)" font-weight="700" font-family="Open Sans,sans-serif">Calorimeter Test per ISO 9151</text>
    <line x1="40" y1="30" x2="40" y2="190" stroke="#888"/>
    <line x1="40" y1="190" x2="280" y2="190" stroke="#888"/>
    <g stroke="#eee"><line x1="40" y1="150" x2="280" y2="150"/><line x1="40" y1="110" x2="280" y2="110"/><line x1="40" y1="70" x2="280" y2="70"/></g>
    <path d="M42 188 C90 180 110 120 140 40" stroke="#e03c31" fill="none" stroke-width="1.5"/>
    <path d="M42 188 C110 178 140 120 175 40" stroke="#f28e2b" fill="none" stroke-width="1.5"/>
    <path d="M42 188 C130 176 170 120 210 40" stroke="#59a14f" fill="none" stroke-width="1.5"/>
    <path d="M42 188 C150 178 200 130 250 50" stroke="#4e79a7" fill="none" stroke-width="1.5"/>
    <text x="130" y="208" font-size="8" fill="#444" font-family="Open Sans,sans-serif">Time (s)</text>
  </svg>
</div>

<div class="band abs"></div>
<h2 class="section-title abs" style="top:1828px">AERODYNAMIC FABRICS</h2>
<p class="section-copy wide abs" style="top:1872px">KRVT developed and patented aerodynamic fabrics, and measured the drag reduction on bicycles in a wind tunnel.</p>
<p class="cta abs" style="top:1908px">If you need to go faster or reduce energy costs, contact us about our DragLow fabric.</p>
<div class="media abs" style="left:450px;top:1950px;height:210px">
  <div class="photo" role="img" aria-label="Cyclist in an aerodynamic skinsuit riding a time trial bike" style="background:linear-gradient(180deg,#b9c3cc 0%,#8a96a2 55%,#4d5660 100%)"></div>
</div>

<footer class="site-footer abs">
  <div class="footer-brand abs"><span class="mark"></span><span class="name">KRVT</span></div>
  <nav class="footer-nav abs"><span>Home</span><span>About Us</span><span>Products</span><span>Solutions</span><span>Contact Us</span></nav>
  <p class="copyright abs">Copyright © 2016 K. R. Vantor and Associates PLLC. All rights reserved.</p>
  <div class="social abs"><span></span><span></span></div>
</footer>

</body>
</html>
```